Kestrel Gardenworks Flyer

I would like to purchase a customized version of a design you have previously submitted - https://www.artbidhub-example.com/design/8374215
Hello,
I like this design a lot. I would change the bullet points to;
- Landscape Design & Construction
- Paver Patio/path installations
- Retaining wall installations
- Pergola Installations
- Grading
- All Hardscape construction
- Drainage specialist
- Yard Maintenance plans
- Mulch & Pine needles
- Bloomin' Great Service!
In the yellow star part - "Mention this flyer for a 10% discount!"
Our logo is attached
Phone number - 7045182094
email - kestrelgardenworks@mailbox-example.com
website - www.kestrelgardenworks-example.com
Target Market(s)
Residential homes in Charlotte, North Carolina
Industry/Entity Type
Landscaping
Look and feel

```html
<!DOCTYPE html>
<html lang="en">
<head>
<meta charset="utf-8">
<title>Kestrel Gardenworks Flyer</title>
<link href="https://fonts.googleapis.com/css2?family=Montserrat:wght@500;600;700;800;900&display=swap" rel="stylesheet">
<style>
  :root {
    --peach-light: #fbd3ae;
    --peach: #f2b07c;
    --brown: #9c5a27;
    --brown-dark: #7d441a;
    --ink: #231a14;
    --gold: #f6c519;
    --cream: #fff6ea;
    --white: #ffffff;
    --backdrop: #ececec;
  }
  html, body {
    margin: 0;
    padding: 0;
    width: 1200px;
    height: 2206px;
    overflow: hidden;
    background: var(--backdrop);
  }
  .canvas {
    position: relative;
    width: 1200px;
    height: 2206px;
  }
  .flyer {
    position: absolute;
    left: 43px;
    top: 384px;
    width: 795px;
    height: 1027px;
    transform: scale(1.4);
    transform-origin: top left;
    background: var(--white);
    overflow: hidden;
    font-family: "Montserrat", sans-serif;
    box-shadow: 0 3px 10px rgba(0,0,0,.25);
  }
  .flyer-shapes, .star-layer {
    position: absolute;
    left: 0;
    top: 0;
    width: 795px;
    height: 1027px;
  }
  .star-layer { pointer-events: none; }
  .brand {
    position: absolute;
    left: 48px;
    top: 78px;
    display: flex;
    align-items: center;
    gap: 10px;
    font-weight: 800;
    font-size: 25px;
    line-height: 1.05;
    color: var(--ink);
  }
  .brand-dot {
    width: 34px;
    height: 34px;
    border-radius: 50%;
    background: var(--brown);
    flex: none;
  }
  .headline {
    position: absolute;
    right: 45px;
    top: 30px;
    text-align: right;
    color: var(--ink);
  }
  .headline-lead {
    font-weight: 900;
    font-size: 43px;
    line-height: 48px;
  }
  .headline-sub {
    font-weight: 800;
    font-size: 34px;
    line-height: 37px;
  }
  .website {
    position: absolute;
    right: 63px;
    top: 166px;
    font-weight: 700;
    font-size: 19px;
    color: var(--ink);
  }
  .services {
    position: absolute;
    left: 50px;
    top: 590px;
    margin: 0;
    padding: 0;
    list-style: none;
    color: var(--cream);
    font-weight: 600;
    font-size: 16.5px;
  }
  .services li {
    position: relative;
    padding-left: 28px;
    line-height: 19px;
    margin-bottom: 13.5px;
  }
  .services li svg {
    position: absolute;
    left: 0;
    top: 2px;
  }
  .call-bar {
    position: absolute;
    left: 49px;
    top: 952px;
    width: 410px;
    height: 57px;
    background: var(--ink);
    border-radius: 12px 4px 4px 12px;
    display: flex;
    align-items: center;
    padding-left: 16px;
    box-sizing: border-box;
    font-weight: 800;
    font-size: 31px;
    color: var(--white);
    white-space: nowrap;
  }
  .call-bar .call-label { color: var(--gold); margin-right: 10px; }
  .discount {
    position: absolute;
    left: 492px;
    top: 783px;
    width: 265px;
    height: 187px;
    background: var(--ink);
    border-radius: 16px;
  }
  .discount-value {
    position: absolute;
    left: 0; right: 0;
    top: 76px;
    text-align: center;
    font-weight: 900;
    font-size: 50px;
    line-height: 52px;
    color: var(--white);
    letter-spacing: -1px;
  }
  .discount-value .mini-star { color: var(--gold); font-size: 34px; vertical-align: 8px; }
  .discount-label {
    position: absolute;
    left: 0; right: 0;
    top: 124px;
    text-align: center;
    font-weight: 900;
    font-size: 34px;
    line-height: 38px;
    color: var(--gold);
  }
  .discount-note {
    position: absolute;
    left: 0; right: 0;
    top: 164px;
    text-align: center;
    font-weight: 600;
    font-size: 10.5px;
    color: var(--cream);
    white-space: nowrap;
  }
  .email {
    position: absolute;
    right: 20px;
    top: 993px;
    font-weight: 600;
    font-size: 10px;
    color: var(--ink);
    white-space: nowrap;
  }
</style>
</head>
<body>
<div class="canvas">
  <div class="flyer">
    <svg class="flyer-shapes" viewBox="0 0 795 1027" xmlns="http://www.w3.org/2000/svg">
      <defs>
        <linearGradient id="headerTone" x1="0" y1="0" x2="1" y2="0">
          <stop offset="0" stop-color="#fbd6b3"/>
          <stop offset="0.45" stop-color="#f3b684"/>
          <stop offset="1" stop-color="#f2b07c"/>
        </linearGradient>
        <linearGradient id="gardenTone" x1="0" y1="0" x2="0" y2="1">
          <stop offset="0" stop-color="#6f9fd4"/>
          <stop offset="0.25" stop-color="#5a8a3a"/>
          <stop offset="0.55" stop-color="#3f7a25"/>
          <stop offset="1" stop-color="#5fa32c"/>
        </linearGradient>
        <linearGradient id="frontYardTone" x1="0" y1="0" x2="0" y2="1">
          <stop offset="0" stop-color="#8a8a86"/>
          <stop offset="0.5" stop-color="#6e7a5a"/>
          <stop offset="1" stop-color="#6aa63a"/>
        </linearGradient>
        <linearGradient id="wallTone" x1="0" y1="0" x2="0" y2="1">
          <stop offset="0" stop-color="#4f8a35"/>
          <stop offset="1" stop-color="#bfae8c"/>
        </linearGradient>
        <linearGradient id="rowShade" x1="0" y1="0" x2="1" y2="0">
          <stop offset="0" stop-color="#6f3c15" stop-opacity="0.55"/>
          <stop offset="1" stop-color="#6f3c15" stop-opacity="0"/>
        </linearGradient>
      </defs>

      <rect x="0" y="0" width="795" height="300" fill="url(#headerTone)"/>

      <path d="M0,235 C180,165 400,175 560,212 C660,236 740,232 795,205 L795,255 C730,275 640,270 540,245 C380,208 180,205 0,260 Z" fill="var(--brown)"/>
      <path d="M480,222 C600,246 720,220 795,160 L795,190 C730,240 610,260 480,222 Z" fill="var(--ink)"/>

      <path d="M0,248 C180,185 400,192 550,228 C660,254 740,250 795,222 L795,620 L0,620 Z" fill="url(#gardenTone)" role="img" aria-label="Photo of a landscaped garden with a curved hedge border, lawn and flowering shrubs"/>

      <rect x="380" y="600" width="415" height="427" fill="var(--white)"/>

      <path d="M0,560 C130,500 300,515 430,590 L470,610 C320,560 150,545 0,590 Z" fill="var(--ink)"/>
      <path d="M0,590 C150,545 320,560 470,610 C485,760 460,900 410,1027 L0,1027 Z" fill="var(--brown)"/>

      <rect x="0" y="645" width="390" height="26" fill="url(#rowShade)"/>
      <rect x="0" y="710" width="390" height="26" fill="url(#rowShade)"/>
      <rect x="0" y="775" width="390" height="26" fill="url(#rowShade)"/>
      <rect x="0" y="840" width="390" height="26" fill="url(#rowShade)"/>
      <rect x="0" y="905" width="390" height="26" fill="url(#rowShade)"/>

      <circle cx="597" cy="625" r="190" fill="var(--white)"/>
      <circle cx="597" cy="625" r="182" fill="url(#frontYardTone)" role="img" aria-label="Photo of a house entrance with stone arch and landscaped walkway"/>

      <circle cx="437" cy="757" r="94" fill="var(--ink)"/>
      <circle cx="437" cy="757" r="89" fill="url(#wallTone)" role="img" aria-label="Photo of a stone retaining wall with garden beds"/>

      <polygon points="455,952 472,945 468,1003 455,1009" fill="var(--ink)"/>
    </svg>

    <div class="brand"><span class="brand-dot"></span><span>Kestrel<br>Gardenworks</span></div>

    <div class="headline">
      <div class="headline-lead">Where 'Bloomin'</div>
      <div class="headline-sub">Great service<br>happens daily!</div>
    </div>
    <div class="website">www.kestrelgardenworks-example.com</div>

    <ul class="services">
      <li><svg width="15" height="15" viewBox="0 0 16 16"><circle cx="8" cy="8" r="8" fill="#fff6ea"/><path d="M4.3,8.3 L7,10.8 L11.8,5.5" stroke="#9c5a27" stroke-width="2.2" fill="none"/></svg>Landscape Design<br>&amp; Construction</li>
      <li><svg width="15" height="15" viewBox="0 0 16 16"><circle cx="8" cy="8" r="8" fill="#fff6ea"/><path d="M4.3,8.3 L7,10.8 L11.8,5.5" stroke="#9c5a27" stroke-width="2.2" fill="none"/></svg>Paver Patio/path installations</li>
      <li><svg width="15" height="15" viewBox="0 0 16 16"><circle cx="8" cy="8" r="8" fill="#fff6ea"/><path d="M4.3,8.3 L7,10.8 L11.8,5.5" stroke="#9c5a27" stroke-width="2.2" fill="none"/></svg>Retaining wall installations</li>
      <li><svg width="15" height="15" viewBox="0 0 16 16"><circle cx="8" cy="8" r="8" fill="#fff6ea"/><path d="M4.3,8.3 L7,10.8 L11.8,5.5" stroke="#9c5a27" stroke-width="2.2" fill="none"/></svg>Pergola Installations</li>
      <li><svg width="15" height="15" viewBox="0 0 16 16"><circle cx="8" cy="8" r="8" fill="#fff6ea"/><path d="M4.3,8.3 L7,10.8 L11.8,5.5" stroke="#9c5a27" stroke-width="2.2" fill="none"/></svg>Grading</li>
      <li><svg width="15" height="15" viewBox="0 0 16 16"><circle cx="8" cy="8" r="8" fill="#fff6ea"/><path d="M4.3,8.3 L7,10.8 L11.8,5.5" stroke="#9c5a27" stroke-width="2.2" fill="none"/></svg>All Hardscape construction</li>
      <li><svg width="15" height="15" viewBox="0 0 16 16"><circle cx="8" cy="8" r="8" fill="#fff6ea"/><path d="M4.3,8.3 L7,10.8 L11.8,5.5" stroke="#9c5a27" stroke-width="2.2" fill="none"/></svg>Drainage specialist</li>
      <li><svg width="15" height="15" viewBox="0 0 16 16"><circle cx="8" cy="8" r="8" fill="#fff6ea"/><path d="M4.3,8.3 L7,10.8 L11.8,5.5" stroke="#9c5a27" stroke-width="2.2" fill="none"/></svg>Yard Maintenance plans</li>
      <li><svg width="15" height="15" viewBox="0 0 16 16"><circle cx="8" cy="8" r="8" fill="#fff6ea"/><path d="M4.3,8.3 L7,10.8 L11.8,5.5" stroke="#9c5a27" stroke-width="2.2" fill="none"/></svg>Mulch &amp; Pine needles</li>
      <li><svg width="15" height="15" viewBox="0 0 16 16"><circle cx="8" cy="8" r="8" fill="#fff6ea"/><path d="M4.3,8.3 L7,10.8 L11.8,5.5" stroke="#9c5a27" stroke-width="2.2" fill="none"/></svg>Bloomin' Great Service!</li>
    </ul>

    <div class="call-bar"><span class="call-label">Call Us:</span>7045182094</div>

    <div class="discount">
      <div class="discount-value"><span class="mini-star">★</span>10%<span class="mini-star">★</span></div>
      <div class="discount-label">DISCOUNT!</div>
      <div class="discount-note">Mention this flyer for a 10% discount!</div>
    </div>

    <svg class="star-layer" viewBox="0 0 795 1027" xmlns="http://www.w3.org/2000/svg">
      <defs>
        <linearGradient id="starGold" x1="0" y1="0" x2="1" y2="1">
          <stop offset="0" stop-color="#fff2a0"/>
          <stop offset="0.5" stop-color="#f2c21a"/>
          <stop offset="1" stop-color="#b07d08"/>
        </linearGradient>
      </defs>
      <polygon points="622,693 641,752 703,752 653,789 672,848 622,812 572,848 591,789 541,752 603,752" fill="url(#starGold)"/>
    </svg>

    <div class="email">Email: kestrelgardenworks@mailbox-example.com</div>
  </div>
</div>
</body>
</html>
```